Slabline Benchworks Australia - Pool Flyer

G'day,Slabline Benchworks Australia sells poolforms (https://www.slablinebenchworksaustralia.com.au/index.php?route=product/category&path=17_61) The poolforms are reusable forms to pour a seamless concrete pool surround instead of using coping tiles. A much better look, less maintenance, and a modern architectural look .We're going to attend a pool and spa show but it is also about landscaping/surround as well. The forms we do make the concrete surround of a pool instead of tiles. I've put some text in a word doc and pictures as well. Feel free to use any words from our website and use/crop pics as you see fit.Any questions, more than happy to answer. We're thinking an A4 tri-fold flyer but happy for other suggestions as well. We're going to attend the show, speak to exhibitors, and hand them the flyer (and maybe a little promo thing too).

Target Market(s)

The target market is we are going to a pool and spa expo. The exhibitors install pools and do backyard landscaping. The flyer is for them.

Colors

Designer to choose colors to be used in the design.

Requirements
Must have
• The text/description of the poolforms and some of the pictures.
• Finished pictures.
• 1 or 2 of the forms (From the website).
• 1 of the Hide skimmer lid pictures (finished is probably better from the jpg with 3 images. probably best to crop and use 1 of the 3.
• Contact details of the website & email contact of sales@slablinebenchworksaustralia.com.au + the phone number.

```html
<!DOCTYPE html>
<html lang="en">
<head>
<meta charset="utf-8">
<title>Slabline Benchworks Australia – Pool Flyer</title>
<link href="https://fonts.googleapis.com/css2?family=Montserrat:wght@400;600;700;800&family=Lobster&family=Open+Sans:wght@400;600;700&display=swap" rel="stylesheet">
<style>
  :root{
    --backdrop:#cfcfcf;
    --white:#ffffff;
    --ink:#1b1b1b;
    --grey-text:#3a3a3a;
    --lavender:#b7b3dc;
    --pool-blue:#2b3ea8;
    --magenta:#c23a9b;
    --purple:#6a2ca0;
    --orange:#f8ab3f;
    --bar:#1f1f1f;
  }
  *{box-sizing:border-box;margin:0;padding:0}
  html,body{width:1200px;height:900px;overflow:hidden;background:var(--backdrop)}
  .flyer{position:absolute;left:368px;top:120px;width:466px;height:662px;background:var(--white);overflow:hidden;font-family:"Open Sans",sans-serif}
  .hero-photo{position:absolute;left:0;top:0;width:466px;height:470px;
    background:linear-gradient(180deg,#1f2722 0%,#2d3a2c 28%,#4e6b3c 40%,#c9c2b3 46%,#2a3fae 52%,#2537a0 100%)}
  .shapes{position:absolute;left:0;top:0}
  .brand{position:absolute;left:18px;top:26px;display:flex;align-items:center;gap:8px}
  .brand-dot{width:30px;height:30px;border:2px solid var(--white);border-radius:50%}
  .brand-name{font-family:"Montserrat",sans-serif;font-weight:400;color:var(--white);font-size:7.5px;letter-spacing:2.4px;line-height:12px;text-transform:uppercase}
  .headline{position:absolute;left:19px;top:82px;font-family:"Montserrat",sans-serif;font-weight:800;color:var(--white);font-size:27px;line-height:29px;letter-spacing:3px;white-space:nowrap}
  .intro{position:absolute;left:0;top:182px;width:296px;height:68px;background:var(--lavender);opacity:.92;border-radius:0 34px 34px 0;padding:4px 14px 0 16px;font-size:12.4px;line-height:13.6px;letter-spacing:1px;color:var(--grey-text)}
  .pour-time{position:absolute;right:10px;top:206px;text-align:right;color:var(--white)}
  .pour-time .lead{font-family:"Montserrat",sans-serif;font-size:17px;letter-spacing:1.4px;line-height:23px}
  .pour-time .hours{font-family:"Lobster",sans-serif;font-size:36px;line-height:46px}
  .shot{position:absolute;background:var(--white);padding:5px;box-shadow:0 2px 5px rgba(0,0,0,.25)}
  .shot .pic{width:100%;height:100px}
  .shot .caption{background:var(--bar);color:var(--white);font-family:"Montserrat",sans-serif;font-weight:700;font-size:5.2px;line-height:6.2px;letter-spacing:.3px;text-align:center;text-transform:uppercase;padding:4px 2px;margin-top:4px;white-space:nowrap}
  .shot-left{left:40px;top:324px;width:120px;transform:rotate(-16deg)}
  .shot-left .pic{background:linear-gradient(135deg,#a9a7a4,#7f7c79 60%,#8fd0e6)}
  .shot-centre{left:168px;top:328px;width:132px}
  .shot-centre .pic{height:112px;background:linear-gradient(180deg,#2b2b2b 0%,#6e7a60 40%,#35a6e0 55%,#d8d5cf 80%,#c3bdb2)}
  .shot-right{left:304px;top:324px;width:120px;transform:rotate(21deg)}
  .shot-right .pic{background:linear-gradient(135deg,#c8ccd2,#9aa0a8 70%,#b8bcc2)}
  .benefits{position:absolute;left:0;top:510px;width:466px;text-align:center;font-family:"Lobster",sans-serif;font-size:13px;line-height:17px;color:var(--grey-text)}
  .benefits .dot{display:inline-block;width:7px;height:7px;border-radius:50%;background:var(--magenta);margin:0 2px 1px 4px}
  .cta{position:absolute;left:0;top:548px;width:466px;text-align:center;font-family:"Montserrat",sans-serif;font-weight:700;font-size:9.4px;letter-spacing:.6px;color:var(--ink)}
  .web-bar{position:absolute;left:0;top:564px;width:466px;height:15px;background:var(--bar);color:var(--white);text-align:center;font-family:"Montserrat",sans-serif;font-weight:700;font-size:8.4px;line-height:15px;letter-spacing:.6px}
  .footer{position:absolute;left:0;top:584px;width:466px;height:78px;background:var(--orange)}
  .footer-curve{position:absolute;left:0;top:0}
  .contact{position:absolute;left:19px;top:11px;color:var(--white)}
  .contact .label{font-family:"Lobster",sans-serif;font-size:15px;line-height:18px}
  .contact .phone{font-family:"Open Sans",sans-serif;font-weight:700;font-size:18px;line-height:22px}
  .contact .email{font-family:"Montserrat",sans-serif;font-weight:700;font-size:7.6px;letter-spacing:.6px;margin-top:3px}
  .find{position:absolute;left:302px;top:6px;color:var(--ink)}
  .find .label{font-family:"Lobster",sans-serif;font-size:14px;line-height:18px;padding-left:16px}
  .find .address{display:flex;gap:4px;font-size:6.6px;line-height:8.4px}
  .mini-brand{position:absolute;right:12px;bottom:12px;display:flex;align-items:center;gap:4px}
  .mini-brand .brand-dot{width:13px;height:13px;border-width:1.4px}
  .mini-brand span{font-family:"Montserrat",sans-serif;font-size:4px;line-height:5px;letter-spacing:.8px;color:var(--white);text-transform:uppercase}
</style>
</head>
<body>
<main class="flyer">
  <div class="hero-photo" role="img" aria-label="Backyard pool with a seamless concrete pool surround, dark fence and striped umbrella"></div>

  <svg class="shapes" width="466" height="662" viewBox="0 0 466 662" aria-hidden="true">
    <defs>
      <linearGradient id="blob-fill" x1="0" y1="0" x2="1" y2="1">
        <stop offset="0" stop-color="#d13f99"/>
        <stop offset="1" stop-color="#5e2a9e"/>
      </linearGradient>
    </defs>
    <path d="M0 420 C60 460 120 500 200 500 C280 500 330 470 466 430 L466 662 L0 662 Z" fill="var(--pool-blue)"/>
    <path d="M310 210 C340 180 420 176 466 186 L466 520 C420 520 360 520 330 500 C290 470 300 420 310 380 C318 330 300 250 310 210 Z" fill="url(#blob-fill)"/>
    <path d="M0 480 C80 500 170 530 260 520 C350 510 420 470 466 470 L466 662 L0 662 Z" fill="var(--white)"/>
  </svg>

  <div class="brand">
    <div class="brand-dot"></div>
    <div class="brand-name">Slabline<br>Benchworks<br>Australia</div>
  </div>

  <h1 class="headline">THE BEST SEAMLESS<br>POOLEDGE FORMING<br>SYSTEM</h1>

  <p class="intro">The Kerb Poolforms are made from strong PVC and can produce architectural designed looks that suit all types of pools.</p>

  <div class="pour-time">
    <div class="lead">ready to for<br>pouring in</div>
    <div class="hours">2 hours!</div>
  </div>

  <figure class="shot shot-left">
    <div class="pic" role="img" aria-label="Close-up of a finished grey concrete pool edge with hidden skimmer lid"></div>
    <figcaption class="caption">Forms are resusable<br>and do not add<br>to landfill</figcaption>
  </figure>
  <figure class="shot shot-centre">
    <div class="pic" role="img" aria-label="Blue pool with a seamless pale concrete surround"></div>
    <figcaption class="caption">Forms are both straight<br>and bendable so no problem<br>for any shaped pool</figcaption>
  </figure>
  <figure class="shot shot-right">
    <div class="pic" role="img" aria-label="Finished concrete pool ledge corner with skimmer lid"></div>
    <figcaption class="caption">Easy to use to<br>create a seamless<br>pooledge</figcaption>
  </figure>

  <div class="benefits">
    <span class="dot"></span>Any Type of Concrete <span class="dot"></span>Any Type of Pool<br>
    <span class="dot"></span>Architectural-designed look <span class="dot"></span>Virtually no maintenance
  </div>

  <p class="cta">GET IN TOUCH WITH US TO GET YOUR HANDS ON THE BEST POOL FORMWORK.</p>
  <div class="web-bar">HTTPS://WWW.SLABLINEBENCHWORKSAUSTRALIA.COM.AU</div>

  <footer class="footer">
    <svg class="footer-curve" width="466" height="78" viewBox="0 0 466 78" aria-hidden="true">
      <path d="M270 0 C300 0 300 50 340 55 C380 60 420 20 466 0 Z" fill="var(--white)"/>
    </svg>
    <div class="contact">
      <div class="label">Contact now!</div>
      <div class="phone">+123 555 0199</div>
      <div class="email">SALES@SLABLINEBENCHWORKSAUSTRALIA.COM.AU</div>
    </div>
    <div class="find">
      <div class="label">Find Us!</div>
      <div class="address">
        <svg width="6" height="8" viewBox="0 0 6 8" aria-hidden="true"><path d="M3 0 C1.3 0 0 1.3 0 3 C0 5 3 8 3 8 C3 8 6 5 6 3 C6 1.3 4.7 0 3 0 Z M3 4.2 A1.2 1.2 0 1 1 3 1.8 A1.2 1.2 0 1 1 3 4.2 Z" fill="var(--ink)"/></svg>
        <span>27 Wattle Bend Road,<br>Geelong VIC 3220</span>
      </div>
    </div>
    <div class="mini-brand">
      <div class="brand-dot"></div>
      <span>Slabline<br>Benchworks<br>Australia</span>
    </div>
  </footer>
</main>
</body>
</html>
```